Hydraulics Company Business Card Design

Modern business card design for a hydraulics company.
Our company colours are - black, orange and white.
I would like the following contact details included-
Name
Position
Phone number
Email
Website
Street Address

I have attached our company logo.
I would like the back of the card white.

Thank you.

```html
<!DOCTYPE html>
<html lang="en">
<head>
<meta charset="UTF-8">
<title>Tallowood Hydraulics – Business Card</title>
<link href="https://fonts.googleapis.com/css2?family=Montserrat:wght@400;500;800&display=swap" rel="stylesheet">
<style>
  :root {
    --bg: #2b2b2b;
    --card-dark: #161616;
    --card-light: #ffffff;
    --ink: #161616;
    --orange: #f7961e;
    --white: #ffffff;
  }
  * { box-sizing: border-box; margin: 0; padding: 0; }
  html, body { width: 1200px; height: 689px; overflow: hidden; }
  body {
    background: var(--bg);
    font-family: "Montserrat", sans-serif;
    display: flex;
    align-items: center;
    justify-content: center;
    gap: 48px;
  }
  .card {
    width: 520px;
    height: 298px;
    border-radius: 22px;
    box-shadow: 0 14px 30px rgba(0,0,0,0.45);
    position: relative;
    overflow: hidden;
  }

  /* Logo side – white */
  .card--logo {
    background: var(--card-light);
    display: flex;
    align-items: center;
    justify-content: center;
  }
  .logo-brand {
    color: var(--ink);
    font-weight: 800;
    font-size: 44px;
    letter-spacing: -0.5px;
    line-height: 1.05;
  }

  /* Contact side – black */
  .card--contact {
    background: var(--card-dark);
    display: flex;
    align-items: center;
    padding: 0 30px 0 34px;
  }
  .contact-brand {
    flex: 0 0 200px;
    color: var(--orange);
    font-weight: 800;
    font-size: 26px;
    line-height: 1.1;
    align-self: flex-end;
    margin-bottom: 70px;
  }
  .divider {
    flex: none;
    width: 1.5px;
    height: 180px;
    background: var(--orange);
    margin: 0 24px 0 10px;
  }
  .details { color: var(--white); font-size: 12.5px; line-height: 1.6; white-space: nowrap; }
  .person-name {
    color: var(--orange);
    font-weight: 800;
    font-size: 21px;
    line-height: 1.15;
  }
  .person-role { font-weight: 500; margin-bottom: 12px; }
  .contact-row { display: flex; align-items: center; gap: 8px; }
  .contact-row svg { width: 11px; height: 11px; fill: var(--orange); flex: none; }
  .address { margin-top: 12px; }
</style>
</head>
<body>
  <section class="card card--logo" aria-label="Card back">
    <div class="logo-brand">Tallowood<br>Hydraulics</div>
  </section>

  <section class="card card--contact" aria-label="Card front">
    <div class="contact-brand">Tallowood<br>Hydraulics</div>
    <div class="divider"></div>
    <div class="details">
      <div class="person-name">Daniel Marsh</div>
      <div class="person-role">Managing Director</div>
      <div class="contact-row">
        <svg viewBox="0 0 24 24" aria-hidden="true"><path d="M6.6 10.8a15 15 0 0 0 6.6 6.6l2.2-2.2c.3-.3.7-.4 1-.2 1.1.4 2.3.6 3.6.6.6 0 1 .4 1 1V20c0 .6-.4 1-1 1A17 17 0 0 1 3 4c0-.6.4-1 1-1h3.5c.6 0 1 .4 1 1 0 1.3.2 2.5.6 3.6.1.3 0 .7-.2 1z"/></svg>
        <span>123 456 789</span>
      </div>
      <div class="contact-row">
        <svg viewBox="0 0 24 24" aria-hidden="true"><path d="M2 5h20v14H2zM3.5 6.5 12 13l8.5-6.5z"/></svg>
        <span>info@yourgmail.com</span>
      </div>
      <div class="contact-row">
        <svg viewBox="0 0 24 24" aria-hidden="true"><circle cx="12" cy="12" r="10"/></svg>
        <span>www.yourwebsite.com</span>
      </div>
      <div class="address">Your address, City<br>State, Zip 1234</div>
    </div>
  </section>
</body>
</html>
```